Redesign website for small print company

Vindaborgprent is a small printing company in Iceland mainly servicing Students, schools, etc. We are also doing all kind of other jobs, like business cards, book printing, brochure printing etc. We are also selling books online.
Our website is: www.vindaborgprent.is
What we are looking for is:
- Web Design (Uncoded - PSD layout only)
- Mobile friendly design, using our current color scheme: Red, green, yellow and light gray.
- Clean simple design
- Simple, light and easy to use.
- More menu Items/drop down
Industry/Entity Type
Digital Printing
Number of Pages Required
5+ page
Requirements
Must have
- Easy navigation
- Designed for mobile
- Current color scheme (see logo)
Nice to have
- Icon based products

```html
<!DOCTYPE html>
<html lang="en">
<head>
<meta charset="utf-8">
<title>Vindaborgprent</title>
<link rel="stylesheet" href="https://fonts.googleapis.com/css2?family=Lato:wght@400;700;900&display=swap">
<style>
:root{
  --red:#e8322b;
  --green:#0f7a3a;
  --yellow:#f7c51e;
  --light:#efefef;
  --mid:#d9d9d9;
  --ink:#222;
  --text:#555;
  --dark:#2b2b2b;
  --darker:#1f1f1f;
  --white:#fff;
}
*{box-sizing:border-box;margin:0;padding:0}
html,body{width:1200px;height:3928px;overflow:hidden}
body{font-family:"Lato",sans-serif;color:var(--ink);background:var(--white);position:relative}
section,header,footer{position:absolute;left:0;width:1200px}
.heading{font-weight:900;font-size:26px;text-align:center;text-transform:uppercase;letter-spacing:.5px}
.heading-rule{display:flex;justify-content:center;margin:12px auto 0;width:120px;height:3px}
.heading-rule span{flex:1}
.heading-rule span:nth-child(1){background:var(--red)}
.heading-rule span:nth-child(2){background:var(--yellow)}
.heading-rule span:nth-child(3){background:var(--green)}

/* header */
.site-header{top:0;height:88px;background:var(--white)}
.brand{position:absolute;left:112px;top:22px;font-weight:700;font-size:28px;color:var(--red)}
.top-info{position:absolute;right:80px;top:10px;display:flex;gap:28px;font-size:13px;color:var(--text);align-items:center}
.top-info span{display:flex;align-items:center;gap:6px}
.main-nav{position:absolute;right:80px;top:52px;display:flex;gap:50px;font-size:15px;font-weight:700;text-transform:uppercase}
.main-nav a{color:var(--ink);text-decoration:none;padding-bottom:8px}
.main-nav a.active{color:var(--red);border-bottom:3px solid var(--red)}

/* hero */
.hero{top:88px;height:502px;background:linear-gradient(110deg,#f3c4d0 0%,#9fd3e6 25%,#f6e58a 45%,#e7a7c8 65%,#b6d7f0 85%,#f4cf8f 100%)}
.hero-copy{position:absolute;left:112px;top:320px}
.hero-title{font-size:38px;font-weight:900;color:var(--red)}
.hero-sub{font-size:20px;font-weight:700;color:var(--white);margin-top:6px;text-shadow:0 1px 2px rgba(0,0,0,.3)}
.hero-mockup{position:absolute;left:560px;top:40px;width:600px;height:420px;background:linear-gradient(135deg,#fafafa,#e3e3e3);box-shadow:0 10px 30px rgba(0,0,0,.25)}
.hero-notch{position:absolute;left:588px;bottom:-12px;width:0;height:0;border-left:12px solid transparent;border-right:12px solid transparent;border-top:12px solid #9fd3e6}

/* welcome */
.welcome{top:590px;height:480px;background:var(--light)}
.welcome-copy{position:absolute;left:112px;top:82px;width:680px}
.welcome-title{font-size:26px;font-weight:900;text-transform:uppercase}
.welcome-title .name{color:var(--red)}
.welcome-copy .heading-rule{margin:10px 0 18px;justify-content:flex-start}
.welcome-copy p{font-size:14px;line-height:1.6;color:var(--text);margin-bottom:14px}
.welcome-copy p.lead{color:var(--ink);font-weight:700}
.btn-dark{display:inline-block;background:var(--ink);color:var(--white);font-size:13px;font-weight:700;padding:9px 16px;margin-top:8px}
.welcome-image{position:absolute;left:820px;top:82px;width:240px;height:300px;background:linear-gradient(160deg,#bdbdbd,#6e6e6e 60%,#e84a3b)}

/* products */
.products{top:1070px;height:650px;background:var(--white)}
.products .heading{margin-top:82px}
.product-grid{position:absolute;left:112px;top:160px;display:grid;grid-template-columns:repeat(3,300px);gap:40px 38px}
.product-card{height:208px;background:var(--light);display:flex;flex-direction:column;align-items:center;justify-content:center;gap:22px}
.product-card.featured{background:var(--white);box-shadow:0 4px 16px rgba(0,0,0,.15)}
.product-icon{width:70px;height:70px;border-radius:50%;border:3px solid var(--yellow);background:var(--white);display:flex;align-items:center;justify-content:center}
.product-name{font-size:16px;font-weight:700;text-transform:uppercase}

/* help */
.help{top:1720px;height:380px;background:var(--mid)}
.help .heading{margin-top:110px}
.help-boxes{position:absolute;left:168px;top:178px;display:flex;gap:32px}
.help-box{width:416px;height:152px;color:var(--white);display:flex;align-items:center;gap:20px;padding:0 26px}
.help-box.red{background:var(--red)}
.help-box.green{background:var(--green)}
.help-icon{width:78px;height:78px;border-radius:50%;background:rgba(255,255,255,.2);display:flex;align-items:center;justify-content:center;flex:none}
.help-title{font-size:18px;font-weight:700}
.help-text{font-size:11px;line-height:1.4;opacity:.9;margin:4px 0 6px}
.help-contact{font-size:20px;font-weight:900}
.help-contact.small{font-size:15px}

/* get started */
.start{top:2100px;height:410px;background:var(--white)}
.start .heading{margin-top:98px}
.steps{position:absolute;left:160px;top:180px;display:flex;gap:40px}
.step{width:200px;height:170px;position:relative}
.step-bg{position:absolute;left:40px;top:30px;width:160px;height:140px;background:var(--light)}
.step-icon{position:absolute;left:20px;top:0;width:80px;height:80px;display:flex;align-items:center;justify-content:center}
.step-label{position:absolute;left:80px;top:90px;font-size:15px;font-weight:700;line-height:1.25;text-align:center;width:110px}
.step-label .first{color:var(--red);font-size:18px}

/* testimonials */
.testimonials{top:2510px;height:350px;background:var(--light)}
.testimonials .heading{margin-top:102px}
.testimonial{position:absolute;left:150px;top:170px;display:flex;gap:36px;width:900px}
.avatar{width:120px;height:120px;border-radius:50%;background:linear-gradient(135deg,#f2d3b8,#b06a4a);flex:none;border:4px solid var(--white)}
.quote-mark{color:var(--red);font-size:40px;font-weight:900;line-height:.6}
.quote-text{font-size:12px;line-height:1.6;color:var(--text);font-style:italic;margin-top:4px}
.quote-meta{display:flex;justify-content:flex-end;gap:10px;align-items:center;margin-top:6px;font-size:12px}
.quote-meta .who{color:var(--red);font-weight:700}
.stars{color:var(--green);letter-spacing:2px}
.dots{position:absolute;left:576px;top:318px;display:flex;gap:8px}
.dots span{width:8px;height:8px;border-radius:50%;background:#bbb}
.dots span.on{background:var(--red)}

/* benefits */
.benefits{top:2860px;height:620px;background:var(--white)}
.benefits .heading{margin-top:66px}
.benefit-frame{position:absolute;left:160px;top:130px;width:880px;height:460px}
.benefit-art{position:absolute;left:320px;top:20px;width:240px;height:420px;background:linear-gradient(180deg,#fbe38a 0%,#f5f1e6 40%,#cfe3cf 100%)}
.benefit{position:absolute;display:flex;align-items:center;gap:16px;font-size:20px;color:var(--ink);line-height:1.2}
.benefit.left{left:10px}
.benefit.right{right:10px;text-align:right}

/* footer */
.footer-stripe{top:3484px;height:8px;display:flex}
.footer-stripe span{flex:1}
.footer-menu{top:3492px;height:60px;background:var(--dark);display:flex;justify-content:center;gap:130px;align-items:center;color:var(--white);font-size:15px}
.footer-main{top:3552px;height:260px;background:var(--darker);color:#ddd}
.footer-col{position:absolute;top:26px;font-size:13px}
.footer-col h4{color:var(--white);font-size:15px;margin-bottom:14px}
.social{display:flex;gap:8px}
.social span{width:26px;height:26px;border-radius:50%}
.footer-brand{margin-top:26px;font-weight:700;font-size:20px;color:var(--white)}
.newsletter{display:flex}
.newsletter .input{width:230px;height:32px;background:var(--white);color:#999;font-size:11px;padding:9px}
.newsletter .send{width:40px;height:32px;background:var(--red);display:flex;align-items:center;justify-content:center}
.accept{display:flex;gap:6px;align-items:center;margin-top:14px;font-size:11px}
.accept span{width:34px;height:20px;background:#555;border-radius:3px}
.contact-line{display:flex;gap:8px;align-items:flex-start;margin-bottom:10px;font-size:12px;line-height:1.4}
.copyright{position:absolute;left:0;width:1200px;top:228px;text-align:center;font-size:11px;color:#999}
.chat-tab{position:absolute;right:20px;top:226px;background:var(--red);color:var(--white);font-size:12px;font-weight:700;padding:8px 14px}
.guarantee{top:3812px;height:116px;background:var(--green);display:flex;justify-content:space-around;align-items:center;padding:0 80px;color:var(--white)}
.guarantee-item{display:flex;align-items:center;gap:14px;font-size:16px;font-weight:700;line-height:1.25}
.guarantee-icon{width:54px;height:54px;border-radius:50%;background:var(--yellow);display:flex;align-items:center;justify-content:center}
</style>
</head>
<body>

<header class="site-header">
  <div class="brand">Vindaborgprent</div>
  <div class="top-info">
    <span><svg width="14" height="14" viewBox="0 0 24 24"><path fill="#e8322b" d="M6.6 10.8a15 15 0 006.6 6.6l2.2-2.2c.3-.3.7-.4 1-.2 1.1.4 2.3.6 3.6.6.6 0 1 .4 1 1V20c0 .6-.4 1-1 1C10.6 21 3 13.4 3 4c0-.6.4-1 1-1h3.5c.6 0 1 .4 1 1 0 1.3.2 2.5.6 3.6.1.3 0 .7-.2 1z"/></svg>5550142</span>
    <span><svg width="14" height="14" viewBox="0 0 24 24"><circle cx="12" cy="12" r="9" fill="none" stroke="#e8322b" stroke-width="2"/><path d="M12 7v5l3 2" stroke="#e8322b" stroke-width="2" fill="none"/></svg>Mon - Fri 9-17</span>
    <span><svg width="16" height="14" viewBox="0 0 24 20"><path d="M1 1h4l3 12h12l3-9H7" fill="none" stroke="#0f7a3a" stroke-width="2"/><circle cx="10" cy="17" r="2" fill="#0f7a3a"/><circle cx="18" cy="17" r="2" fill="#0f7a3a"/></svg></span>
  </div>
  <nav class="main-nav">
    <a class="active">Home</a><a>Services</a><a>Job Submit</a><a>About Us</a>
  </nav>
</header>

<section class="hero">
  <div class="hero-mockup" role="img" aria-label="Printed stationery set: letterhead, business cards, envelope and notebook"></div>
  <div class="hero-copy">
    <div class="hero-title">Stand out from the Crowd.</div>
    <div class="hero-sub">Personal Attention. Custom Results.</div>
  </div>
  <div class="hero-notch"></div>
</section>

<section class="welcome">
  <div class="welcome-copy">
    <h1 class="welcome-title">Welcome to <span class="name">Vindaborgprent</span></h1>
    <div class="heading-rule"><span></span><span></span><span></span></div>
    <p class="lead">Our print shop sits right on campus and has specialised in serving students and school staff, while also offering general printing to the public.</p>
    <p>We print essays, theses, business cards, leaflets, posters and books, working on modern digital presses to keep quality high and turnaround short. Whether you need a single copy or a large run, our team helps with layout, paper choice and finishing.</p>
    <p>We are a small, friendly print house with years of experience, and we know what it takes to deliver good work on time.</p>
    <span class="btn-dark">Read More</span>
  </div>
  <div class="welcome-image" role="img" aria-label="Printing press rollers and colour swatch fan"></div>
</section>

<section class="products">
  <h2 class="heading">Our Products</h2>
  <div class="heading-rule"><span></span><span></span><span></span></div>
  <div class="product-grid">
    <div class="product-card featured"><div class="product-icon"><svg width="30" height="34" viewBox="0 0 30 34"><path d="M3 2h16l8 8v22H3z" fill="none" stroke="#e8322b" stroke-width="2.5"/><path d="M8 16h14M8 21h14M8 26h10" stroke="#e8322b" stroke-width="2"/></svg></div><div class="product-name">Essays</div></div>
    <div class="product-card"><div class="product-icon"><svg width="34" height="28" viewBox="0 0 34 28"><rect x="2" y="4" width="30" height="20" rx="2" fill="none" stroke="#e8322b" stroke-width="2.5"/><path d="M7 11h10M7 16h16" stroke="#e8322b" stroke-width="2"/></svg></div><div class="product-name">Business Cards</div></div>
    <div class="product-card"><div class="product-icon"><svg width="34" height="30" viewBox="0 0 34 30"><path d="M2 4l10 3 10-3 10 3v20l-10-3-10 3-10-3z" fill="none" stroke="#e8322b" stroke-width="2.5"/><path d="M12 7v20M22 4v20" stroke="#e8322b" stroke-width="2"/></svg></div><div class="product-name">Leaflets</div></div>
    <div class="product-card"><div class="product-icon"><svg width="34" height="30" viewBox="0 0 34 30"><path d="M17 6c-4-3-10-3-15-1v22c5-2 11-2 15 1 4-3 10-3 15-1V5c-5-2-11-2-15 1zM17 6v22" fill="none" stroke="#e8322b" stroke-width="2.5"/></svg></div><div class="product-name">Book Printing</div></div>
    <div class="product-card"><div class="product-icon"><svg width="30" height="34" viewBox="0 0 30 34"><rect x="3" y="2" width="24" height="30" fill="none" stroke="#e8322b" stroke-width="2.5"/><path d="M7 24l6-8 5 5 4-4 3 7z" fill="#e8322b"/></svg></div><div class="product-name">Posters</div></div>
    <div class="product-card"><div class="product-icon"><svg width="32" height="32" viewBox="0 0 32 32"><rect x="4" y="4" width="10" height="24" fill="none" stroke="#e8322b" stroke-width="2.5"/><rect x="17" y="4" width="10" height="24" fill="none" stroke="#e8322b" stroke-width="2.5"/></svg></div><div class="product-name">Textbooks</div></div>
  </div>
</section>

<section class="help">
  <h2 class="heading">We are here to help you</h2>
  <div class="heading-rule"><span></span><span></span><span></span></div>
  <div class="help-boxes">
    <div class="help-box red">
      <div class="help-icon"><svg width="38" height="38" viewBox="0 0 24 24"><path fill="#fff" d="M6.6 10.8a15 15 0 006.6 6.6l2.2-2.2c.3-.3.7-.4 1-.2 1.1.4 2.3.6 3.6.6.6 0 1 .4 1 1V20c0 .6-.4 1-1 1C10.6 21 3 13.4 3 4c0-.6.4-1 1-1h3.5c.6 0 1 .4 1 1 0 1.3.2 2.5.6 3.6.1.3 0 .7-.2 1z"/></svg></div>
      <div><div class="help-title">Get Real-time Design Help</div><div class="help-text">Send files or chat with our designers to adjust your print job before printing.</div><div class="help-contact">5550142</div></div>
    </div>
    <div class="help-box green">
      <div class="help-icon"><svg width="40" height="32" viewBox="0 0 40 32"><rect x="4" y="10" width="32" height="18" fill="none" stroke="#fff" stroke-width="2.5"/><path d="M4 10l6-7h20l6 7M16 10v6h8v-6" fill="none" stroke="#fff" stroke-width="2.5"/></svg></div>
      <div><div class="help-title">For Bulk Order</div><div class="help-text">Need larger runs for your school or office? Send us a request.</div><div class="help-contact small">prent@vindaborgprent.is</div></div>
    </div>
  </div>
</section>

<section class="start">
  <h2 class="heading">Get Started</h2>
  <div class="heading-rule"><span></span><span></span><span></span></div>
  <div class="steps">
    <div class="step"><div class="step-bg"></div><div class="step-icon"><svg width="60" height="60" viewBox="0 0 60 60"><circle cx="30" cy="30" r="28" fill="#f7c51e"/><path d="M30 14l12 14h-7v14H25V28h-7z" fill="#fff"/></svg></div><div class="step-label"><span class="first">U</span>pload<br>your design</div></div>
    <div class="step"><div class="step-bg"></div><div class="step-icon"><svg width="50" height="60" viewBox="0 0 50 60"><path d="M4 4h30l12 12v40H4z" fill="#fff" stroke="#e8322b" stroke-width="3"/><path d="M12 26h26M12 34h26M12 42h18" stroke="#e8322b" stroke-width="3"/></svg></div><div class="step-label"><span class="first">U</span>se Our<br>Free Templates</div></div>
    <div class="step"><div class="step-bg"></div><div class="step-icon"><svg width="64" height="56" viewBox="0 0 64 56"><rect x="3" y="3" width="58" height="38" rx="3" fill="#fff" stroke="#e8322b" stroke-width="3"/><path d="M24 52h16M32 41v11" stroke="#e8322b" stroke-width="3"/><path d="M18 32l18-18 6 6-18 18h-6z" fill="#e8322b"/></svg></div><div class="step-label"><span class="first">C</span>ustom Your<br>Design</div></div>
    <div class="step"><div class="step-bg"></div><div class="step-icon"><svg width="56" height="56" viewBox="0 0 56 56"><rect x="4" y="22" width="20" height="30" fill="#222"/><rect x="28" y="10" width="22" height="42" fill="#222"/><rect x="10" y="4" width="16" height="16" fill="#222"/></svg></div><div class="step-label"><span class="first">B</span>ulk<br>Enquiry</div></div>
  </div>
</section>

<section class="testimonials">
  <h2 class="heading">What people say about us?</h2>
  <div class="heading-rule"><span></span><span></span><span></span></div>
  <div class="testimonial">
    <div class="avatar" role="img" aria-label="Portrait photo of a customer"></div>
    <div>
      <div class="quote-mark">“</div>
      <p class="quote-text">Our thesis was printed and bound within a day, and the result looked better than we had hoped. The staff checked every page, suggested a better paper and kept the price fair. We will be back for the next project and recommend them to every student we know.</p>
      <div class="quote-meta"><span class="who">Anna Sigurdardottir</span><span class="stars">★★★★★</span></div>
    </div>
  </div>
  <div class="dots"><span class="on"></span><span></span><span></span></div>
</section>

<section class="benefits">
  <h2 class="heading">We make your printlife better</h2>
  <div class="heading-rule"><span></span><span></span><span></span></div>
  <div class="benefit-frame">
    <svg width="880" height="460" style="position:absolute;left:0;top:0">
      <path d="M0 20H880" stroke="#f7c51e" stroke-width="3"/>
      <path d="M0 440H880" stroke="#f7c51e" stroke-width="3"/>
      <path d="M0 20V440M880 20V440" stroke="#e6e6e6" stroke-width="3"/>
      <path d="M20 150H320M560 150H860M20 330H320M560 330H860" stroke="#0f7a3a" stroke-width="2"/>
      <circle cx="860" cy="20" r="6" fill="#0f7a3a"/><circle cx="20" cy="440" r="6" fill="#e8322b"/>
    </svg>
    <div class="benefit-art" role="img" aria-label="Illustration of printed shapes in yellow and green"></div>
    <div class="benefit left" style="top:70px"><svg width="46" height="40" viewBox="0 0 46 40"><rect x="2" y="6" width="42" height="28" rx="3" fill="#222"/><rect x="2" y="12" width="42" height="6" fill="#e8322b"/></svg><span>Secured<br>Payment</span></div>
    <div class="benefit right" style="top:70px"><span>Eco Friendly<br>Materials</span><svg width="44" height="44" viewBox="0 0 44 44"><path d="M6 38C6 16 22 6 40 6c0 20-12 32-34 32z" fill="#0f7a3a"/><circle cx="30" cy="32" r="9" fill="#f7c51e"/></svg></div>
    <div class="benefit left" style="top:250px"><svg width="44" height="44" viewBox="0 0 44 44"><path d="M6 38l4-12 22-22 8 8-22 22z" fill="#0f7a3a"/><path d="M4 40l6-2-4-4z" fill="#e8322b"/></svg><span>Creating Designs<br>Of Your Own</span></div>
    <div class="benefit right" style="top:250px"><span>Home Delivery<br>Options</span><svg width="52" height="40" viewBox="0 0 52 40"><rect x="2" y="6" width="30" height="24" fill="#e8322b"/><path d="M32 14h10l8 8v8H32z" fill="#e8322b"/><circle cx="12" cy="33" r="5" fill="#222"/><circle cx="40" cy="33" r="5" fill="#222"/></svg></div>
  </div>
</section>

<footer class="footer-stripe"><span style="background:var(--red)"></span><span style="background:var(--yellow)"></span><span style="background:var(--green)"></span><span style="background:var(--red)"></span><span style="background:var(--yellow)"></span><span style="background:var(--green)"></span></footer>

<footer class="footer-menu">
  <span>Let Us Help ▾</span><span>What We Offer ▾</span><span>Our Company ▾</span><span>Our Policies ▾</span>
</footer>

<footer class="footer-main">
  <div class="footer-col" style="left:112px">
    <h4>Connect With Us</h4>
    <div class="social"><span style="background:#3b5b9a"></span><span style="background:#d44"></span><span style="background:#2aa3e0"></span><span style="background:#c33"></span></div>
    <div class="footer-brand">Vindaborgprent</div>
  </div>
  <div class="footer-col" style="left:460px">
    <h4>Sign Up For Newsletter</h4>
    <div class="newsletter"><div class="input">Enter Your Email Here</div><div class="send"><svg width="16" height="12" viewBox="0 0 16 12"><rect x="1" y="1" width="14" height="10" fill="none" stroke="#fff" stroke-width="1.5"/><path d="M1 1l7 5 7-5" fill="none" stroke="#fff" stroke-width="1.5"/></svg></div></div>
    <div class="accept">We Accept <span></span><span></span><span></span></div>
  </div>
  <div class="footer-col" style="left:810px">
    <h4>Contact Details</h4>
    <div class="contact-line"><svg width="12" height="16" viewBox="0 0 12 16"><path d="M6 0a6 6 0 016 6c0 4-6 10-6 10S0 10 0 6a6 6 0 016-6z" fill="#e8322b"/></svg><span><b>Vindaborgprent</b><br>Lyngbrekka 4, 310 Vindabær</span></div>
    <div class="contact-line"><svg width="12" height="12" viewBox="0 0 24 24"><path fill="#e8322b" d="M6.6 10.8a15 15 0 006.6 6.6l2.2-2.2c.3-.3.7-.4 1-.2 1.1.4 2.3.6 3.6.6.6 0 1 .4 1 1V20c0 .6-.4 1-1 1C10.6 21 3 13.4 3 4c0-.6.4-1 1-1h3.5c.6 0 1 .4 1 1 0 1.3.2 2.5.6 3.6.1.3 0 .7-.2 1z"/></svg><span>5550142</span></div>
    <div class="contact-line"><svg width="12" height="10" viewBox="0 0 16 12"><rect x="1" y="1" width="14" height="10" fill="none" stroke="#e8322b" stroke-width="2"/></svg><span>prent@vindaborgprent.is</span></div>
  </div>
  <div class="copyright">Copyright © 2024 Vindaborgprent. All Rights Reserved.</div>
  <div class="chat-tab">Offline - Leave a Message</div>
</footer>

<footer class="guarantee">
  <div class="guarantee-item"><div class="guarantee-icon"><svg width="28" height="28" viewBox="0 0 24 24"><circle cx="12" cy="12" r="9" fill="none" stroke="#222" stroke-width="2"/><path d="M12 7v5l3 2" stroke="#222" stroke-width="2" fill="none"/></svg></div><span>Fast Turnaround<br>Within Days</span></div>
  <div class="guarantee-item"><div class="guarantee-icon"><svg width="30" height="24" viewBox="0 0 52 40"><rect x="2" y="6" width="30" height="24" fill="#222"/><path d="M32 14h10l8 8v8H32z" fill="#222"/><circle cx="12" cy="33" r="5" fill="#222"/><circle cx="40" cy="33" r="5" fill="#222"/></svg></div><span>Nationwide<br>Delivery</span></div>
  <div class="guarantee-item"><div class="guarantee-icon"><svg width="26" height="26" viewBox="0 0 24 24"><path d="M4 12l5 5 11-11" fill="none" stroke="#222" stroke-width="3"/></svg></div><span>100% Quality<br>Products Guaranteed</span></div>
</footer>

</body>
</html>
```